Restaurant menu design

I need a menu for a restaurant in Spain.
It has to be bohemian but modern. We need something romantic and elegant.
The restaurant is elegant with good food and an excellent reputation. It is also modern at the same time.
The restaurant is superbly decorated and very chick so we need something "class" to fit in with the surroundings.
The size of the document must be 325 mm in high and 245 mm as a maximum and preferably made in indesign.

Reason: Thank you all for your designs.
So far all your designs are ok but it isn´t what we are looking for. Most of the designs are too loaded, too many colors and too much decoration.

Target Market(s)

Adults of various age groups and different nationalities mostly European.

Industry/Entity Type

Restaurant

Requirements
Must have
• The menu must have two interior pages with the text as in the document attached.It must be easily legible.
Nice to have
• See what kind of menus they use in important restaurants in places like Paris, see what designs are in trend, but Not necessarily doing the same style if it doesn’t fit in with the description above.
Should not have
• Nothing old fashioned.

```html
<!DOCTYPE html>
<html lang="en">
<head>
<meta charset="utf-8">
<title>la violette — menu cover</title>
<link rel="stylesheet" href="https://fonts.googleapis.com/css2?family=Cormorant+Garamond:wght@500&display=swap">
<style>
  :root {
    --backdrop: #ffffff;
    --wood-dark: #5a140a;
    --wood-mid: #7e2312;
    --wood-light: #9a3119;
    --grain-dark: #4a0f07;
    --grain-light: #b0452a;
    --plum-band: #a0508a;
    --plum-band-deep: #7a3466;
    --edge-light: #f6cde8;
    --pink-glow: #f6d3ea;
    --pink-light: #eab4da;
    --pink-mid: #df9dcd;
    --pink-deep: #cf78bb;
    --pattern-tone: #f1bfe0;
    --mark-plum: #9a4a86;
    --ink: #150f13;
  }
  html, body {
    margin: 0;
    padding: 0;
    width: 1200px;
    height: 900px;
    overflow: hidden;
    background: var(--backdrop);
  }
  .canvas {
    position: relative;
    width: 1200px;
    height: 900px;
    overflow: hidden;
  }
  .menu-cover {
    position: absolute;
    left: 248px;
    top: 0;
    width: 686px;
    height: 900px;
  }
  .menu-cover svg {
    display: block;
    width: 686px;
    height: 900px;
  }
  .brand {
    position: absolute;
    left: 0;
    top: 0;
    width: 686px;
    height: 900px;
    pointer-events: none;
  }
  .brand-mark {
    position: absolute;
    left: 252px;
    top: 416px;
    width: 34px;
    height: 34px;
    border-radius: 50%;
    background: var(--mark-plum);
  }
  .brand-name {
    position: absolute;
    left: 300px;
    top: 372px;
    margin: 0;
    font-family: "Cormorant Garamond", Georgia, serif;
    font-weight: 500;
    font-size: 66px;
    line-height: 56px;
    letter-spacing: 2px;
    color: var(--ink);
  }
  .brand-name .line-article {
    display: block;
    padding-left: 18px;
  }
  .brand-name .line-word {
    display: block;
  }
</style>
</head>
<body>
<div class="canvas">
  <section class="menu-cover">
    <svg viewBox="0 0 686 900" xmlns="http://www.w3.org/2000/svg">
      <defs>
        <linearGradient id="wood" x1="0" y1="0" x2="1" y2="0">
          <stop offset="0" stop-color="var(--wood-mid)"/>
          <stop offset="0.25" stop-color="var(--wood-light)"/>
          <stop offset="0.5" stop-color="var(--wood-mid)"/>
          <stop offset="0.75" stop-color="var(--wood-dark)"/>
          <stop offset="1" stop-color="var(--wood-mid)"/>
        </linearGradient>
        <pattern id="grain" width="46" height="900" patternUnits="userSpaceOnUse">
          <rect x="2" width="1.5" height="900" fill="var(--grain-dark)" opacity="0.45"/>
          <rect x="7" width="1" height="900" fill="var(--grain-light)" opacity="0.35"/>
          <rect x="13" width="2.5" height="900" fill="var(--grain-dark)" opacity="0.3"/>
          <rect x="19" width="1" height="900" fill="var(--grain-light)" opacity="0.4"/>
          <rect x="24" width="1.5" height="900" fill="var(--grain-dark)" opacity="0.5"/>
          <rect x="31" width="3" height="900" fill="var(--grain-dark)" opacity="0.2"/>
          <rect x="37" width="1" height="900" fill="var(--grain-light)" opacity="0.3"/>
          <rect x="42" width="1.5" height="900" fill="var(--grain-dark)" opacity="0.4"/>
        </pattern>
        <radialGradient id="pink-field" cx="0.45" cy="0.5" r="0.75">
          <stop offset="0" stop-color="var(--pink-glow)"/>
          <stop offset="0.35" stop-color="var(--pink-light)"/>
          <stop offset="0.75" stop-color="var(--pink-mid)"/>
          <stop offset="1" stop-color="var(--pink-deep)"/>
        </radialGradient>
        <radialGradient id="pattern-glow" cx="0.5" cy="0.5" r="0.5">
          <stop offset="0" stop-color="var(--pattern-tone)" stop-opacity="0.75"/>
          <stop offset="1" stop-color="var(--pattern-tone)" stop-opacity="0"/>
        </radialGradient>
      </defs>

      <g class="wood-panel" role="img" aria-label="Dark red wood grain panel">
        <rect width="686" height="900" fill="url(#wood)"/>
        <rect width="686" height="900" fill="url(#grain)"/>
      </g>

      <path class="wave-band" fill="var(--plum-band)"
        d="M0,78 C150,62 280,96 430,76 C540,62 620,48 686,52
           L686,790 C580,772 460,760 340,768 C210,778 100,800 0,820 Z"/>

      <path class="wave-field" fill="url(#pink-field)" role="img"
        aria-label="Soft pink field with faint flowers, rings, dots and sun rays"
        d="M0,128 C150,104 280,132 430,110 C540,94 620,80 686,80
           L686,748 C580,740 460,730 340,740 C210,750 100,770 0,790 Z"/>

      <g class="pattern-area" role="img" aria-label="Faint decorative pattern of flowers, rings and dotted circles">
        <circle cx="360" cy="470" r="190" fill="url(#pattern-glow)"/>
        <circle cx="570" cy="230" r="120" fill="url(#pattern-glow)" opacity="0.6"/>
        <circle cx="110" cy="280" r="110" fill="url(#pattern-glow)" opacity="0.5"/>
        <circle cx="160" cy="640" r="100" fill="url(#pattern-glow)" opacity="0.5"/>
        <circle cx="540" cy="600" r="110" fill="url(#pattern-glow)" opacity="0.5"/>
      </g>

      <path class="wave-edge" fill="none" stroke="var(--edge-light)" stroke-width="2"
        d="M0,128 C150,104 280,132 430,110 C540,94 620,80 686,80"/>
      <path class="wave-edge" fill="none" stroke="var(--edge-light)" stroke-width="2"
        d="M686,748 C580,740 460,730 340,740 C210,750 100,770 0,790"/>

      <path class="wave-edge-outer" fill="none" stroke="var(--plum-band-deep)" stroke-width="3"
        d="M0,78 C150,62 280,96 430,76 C540,62 620,48 686,52"/>
      <path class="wave-edge-outer" fill="none" stroke="var(--plum-band-deep)" stroke-width="3"
        d="M686,790 C580,772 460,760 340,768 C210,778 100,800 0,820"/>
    </svg>

    <div class="brand">
      <span class="brand-mark" aria-hidden="true"></span>
      <h1 class="brand-name"><span class="line-article">la</span><span class="line-word">violette</span></h1>
    </div>
  </section>
</div>
</body>
</html>
```